Vantrel Web Services

This is a new It services company operating in Perth western Australia

we need a website that is easy to navigate without a cluttered feel to it it should have the following links and pages

About Us
Services
Clients
Contact Us
MY Vantrel (login for clients)

Hi it is a web based IT services company so we would expect customers to come to the website for 2 different purposes the first is to enquire about our services and then as they become customers come to our website to manage their services so whilst they are seperate we want do not want it to look like 2 different websites

hope this helps

Hi to update this we need a home page and templates for sub pages

this is a design brief only and not the coding of the pages or building of the site

```html
<!DOCTYPE html>
<html lang="en">
<head>
<meta charset="utf-8">
<title>Vantrel Web Services</title>
<link href="https://fonts.googleapis.com/css2?family=Arimo:wght@400;700&family=Michroma&family=Roboto:wght@300;400&family=Ubuntu:wght@400;500&display=swap" rel="stylesheet">
<style>
:root{
  --brand-red:#b3070b;
  --brand-red-dark:#7e0306;
  --brand-blue:#002d96;
  --ink:#333;
  --muted:#666;
  --link-blue:#0a3aa0;
  --footer-bg:#111;
  --footer-link:#1c63d8;
  --white:#fff;
}
*{margin:0;padding:0;box-sizing:border-box}
html,body{width:1023px;height:1200px;overflow:hidden;background:var(--white)}
body{position:relative;font-family:"Arimo",Arial,sans-serif;color:var(--ink)}
.abs{position:absolute}

.site-header{position:absolute;left:0;top:0;width:1023px;height:66px;background:linear-gradient(#fff,#e2e2e2);border-bottom:1px solid #999}
.brand-name{position:absolute;left:120px;top:18px;font-family:"Arimo",Arial,sans-serif;font-weight:700;font-size:26px;line-height:30px;color:var(--brand-blue)}
.utility-links{position:absolute;right:117px;top:43px;font-size:9.5px;color:#333}
.utility-links span{margin:0 4px}

.main-nav{position:absolute;left:0;top:66px;width:1023px;height:42px;background:linear-gradient(#2a2a2a,#111);border-bottom:2px solid #000}
.nav-item{position:absolute;top:9px;width:126px;height:23px;border-radius:9px;background:linear-gradient(#d8191d,var(--brand-red-dark));color:#fff;font-family:"Michroma",sans-serif;font-size:9.5px;display:flex;align-items:center;justify-content:center;box-shadow:inset 0 1px 0 rgba(255,255,255,.3)}
.nav-item.is-active{background:linear-gradient(#3563bd,#163c8a)}

.hero-photo{position:absolute;left:0;top:108px;width:1023px;height:345px;background:radial-gradient(circle at 50% 45%,#e6eefc 0%,#7f9fdc 25%,#2f57b0 60%,#1a3174 100%)}

.pillars{position:absolute;left:0;top:453px;width:1023px;height:229px;background:var(--brand-blue)}
.pillar{position:absolute;top:0;width:260px;text-align:center;color:#fff}
.pillar-badge{position:absolute;top:-26px;left:79px;width:102px;height:102px;border-radius:50%;background:radial-gradient(circle at 50% 35%,#fff,#dcdcdc);border:2px solid #0b1d55;display:flex;align-items:center;justify-content:center}
.pillar h2{position:absolute;top:95px;width:100%;font-family:"Roboto",sans-serif;font-weight:300;font-size:31px}
.pillar p{position:absolute;top:138px;width:100%;font-size:12px;line-height:14.5px}

.section-title{font-family:"Roboto",sans-serif;font-weight:300;font-size:31px;color:#111}
.why{left:116px;top:722px}
.why-intro{left:116px;top:763px;width:480px;font-size:12px;line-height:14px}
.why-photo{left:118px;top:806px;width:154px;height:128px;border:2px solid #ccc;background:linear-gradient(135deg,#8fa9c8,#d9e2ee 50%,#40587a)}
.why-body{left:287px;top:809px;width:308px;font-size:12px;line-height:14.5px}
.read-more{left:287px;top:905px;font-size:12px;color:var(--brand-red)}

.news{left:661px;top:722px}
.news-item{position:absolute;left:661px;width:260px}
.news-date{position:absolute;left:0;top:0;width:28px;text-align:center}
.news-day{width:28px;height:28px;border-radius:50%;background:var(--brand-red);color:#fff;font-family:"Ubuntu",sans-serif;font-weight:500;font-size:14px;display:flex;align-items:center;justify-content:center;box-shadow:0 0 0 2px #fff,0 0 0 3px #ddd}
.news-month{margin-top:5px;font-size:10px;font-weight:700;color:var(--brand-red)}
.news-item h3{position:absolute;left:47px;top:0;width:215px;font-size:12px;line-height:14.5px;color:var(--link-blue)}
.news-item p{position:absolute;left:47px;top:33px;width:215px;font-size:10.5px;line-height:12px;color:var(--muted)}
.news-rule{position:absolute;left:2px;top:77px;width:258px;border-top:1px dotted #777}

.site-footer{position:absolute;left:0;top:1035px;width:1023px;height:165px;background:var(--footer-bg)}
.footer-brand{position:absolute;left:100px;top:30px;font-family:"Arimo",Arial,sans-serif;font-weight:700;font-size:20px;line-height:24px;color:#fff}
.footer-col{position:absolute;top:27px}
.footer-col h4{font-family:"Ubuntu",sans-serif;font-weight:400;font-size:15px;color:#fff;margin-bottom:10px}
.footer-col li{list-style:none;font-size:10.5px;color:var(--footer-link);height:18.7px;padding-left:10px;position:relative}
.footer-col li::before{content:"";position:absolute;left:0;top:4px;border-left:3px solid #fff;border-top:2.5px solid transparent;border-bottom:2.5px solid transparent}
.newsletter-input{position:absolute;left:732px;top:1089px;width:157px;height:21px;background:#1d1d1d;border:1px solid #3a3a3a;border-radius:3px;color:#888;font-size:10.5px;padding:4px 12px}
.subscribe{position:absolute;left:825px;top:1119px;width:68px;height:23px;border-radius:4px;background:linear-gradient(#2b8bff,#0a5fd8);color:#fff;font-family:"Ubuntu",sans-serif;font-size:10.5px;font-weight:500;display:flex;align-items:center;justify-content:center}
</style>
</head>
<body>

<header class="site-header">
  <div class="brand-name">Vantrel</div>
  <div class="utility-links">Support<span>|</span>FAQs<span>|</span>Testimonials<span>|</span>Help</div>
</header>

<nav class="main-nav">
  <div class="nav-item is-active" style="left:120px">HOME</div>
  <div class="nav-item" style="left:252px">ABOUT US</div>
  <div class="nav-item" style="left:385px">SERVICES</div>
  <div class="nav-item" style="left:517px">CLIENTS</div>
  <div class="nav-item" style="left:649px">CONTACT US</div>
  <div class="nav-item" style="left:781px">MY VANTREL</div>
</nav>

<div class="hero-photo" role="img" aria-label="Business person touching a glowing digital interface with blue light rings"></div>

<section class="pillars">
  <div class="pillar" style="left:99px">
    <div class="pillar-badge">
      <svg width="46" height="52" viewBox="0 0 46 52"><path d="M23 2 L43 9 V26 C43 38 34 46 23 50 C12 46 3 38 3 26 V9 Z" fill="none" stroke="#0a2f93" stroke-width="4"/><path d="M23 9 L36 13 V26 C36 34 30 40 23 43 Z" fill="#0a2f93"/></svg>
    </div>
    <h2>ADVANTAGES</h2>
    <p>Lorem ipsum dolor sit amet, consectetur adipisicing elit, sed do eiusmod tempor incididunt ut labore et dolore magna aliqua.</p>
  </div>
  <div class="pillar" style="left:380px">
    <div class="pillar-badge">
      <svg width="56" height="56" viewBox="0 0 56 56"><circle cx="28" cy="28" r="23" fill="none" stroke="#0a2f93" stroke-width="9" stroke-dasharray="120 25"/><rect x="19" y="28" width="5" height="10" fill="#0a2f93"/><rect x="26" y="22" width="5" height="16" fill="#0a2f93"/><rect x="33" y="18" width="5" height="20" fill="#0a2f93"/></svg>
    </div>
    <h2>MISSION</h2>
    <p>Sed ut perspiciatis, unde omnis iste natus error sit voluptatem accusantium doloremque laudantium, totam rem aperiam.</p>
  </div>
  <div class="pillar" style="left:659px">
    <div class="pillar-badge">
      <svg width="62" height="62" viewBox="0 0 62 62" fill="#0a2f93"><circle cx="31" cy="31" r="14"/><g><path d="M31 2 l6 8 h-12z"/><path d="M31 60 l6 -8 h-12z"/><path d="M2 31 l8 6 v-12z"/><path d="M60 31 l-8 6 v-12z"/><path d="M10 10 l10 2 -8 8z"/><path d="M52 10 l-2 10 -8 -8z"/><path d="M10 52 l2 -10 8 8z"/><path d="M52 52 l-10 -2 8 -8z"/></g></svg>
    </div>
    <h2>VISION</h2>
    <p>Lorem ipsum dolor sit amet, consectetur adipisicing elit, sed do eiusmod tempor incididunt ut labore et dolore magna aliqua.</p>
  </div>
</section>

<h2 class="abs section-title why">WHY CHOOSE VANTREL?</h2>
<p class="abs why-intro">At vero eos et accusamus et iusto odio dignissimos ducimus, qui blanditiis praesentium voluptatum deleniti atque corrupti, quos dolores et quas molestias excepturi sint.</p>
<div class="abs why-photo" role="img" aria-label="Hands of a business person typing on a laptop keyboard"></div>
<p class="abs why-body">Obcaecati cupiditate non provident, similique sunt in culpa, qui officia deserunt mollitia animi, id est laborum et dolorum fuga.At vero eos et accusamus et iusto odio dignissimos ducimus, qui blanditiis praesentium voluptatum deleniti atque corrupti, quos dolores et quas molestias excepturi sint.</p>
<a class="abs read-more">read more +</a>

<h2 class="abs section-title news">LATEST NEWS</h2>
<article class="news-item" style="top:773px">
  <div class="news-date"><div class="news-day">27</div><div class="news-month">Mar</div></div>
  <h3>We develop our own sofrtware APPS and offer business and IT services</h3>
  <p>Lorem ipsum dolor sit amet, consectetur adipisicing elit, sed do eiusmod tempor incididunt ut labore et dolore magna aliqua.</p>
  <div class="news-rule"></div>
</article>
<article class="news-item" style="top:875px">
  <div class="news-date"><div class="news-day">12</div><div class="news-month">Feb</div></div>
  <h3>We develop our own sofrtware APPS and offer business and IT services</h3>
  <p>Lorem ipsum dolor sit amet, consectetur adipisicing elit, sed do eiusmod tempor incididunt ut labore et dolore magna aliqua.</p>
  <div class="news-rule"></div>
</article>

<footer class="site-footer">
  <div class="footer-brand">Vantrel</div>
  <div class="footer-col" style="left:289px"><h4>Why Us</h4><ul><li>Our Clients</li><li>Technology</li><li>Soft Labs</li></ul></div>
  <div class="footer-col" style="left:391px"><h4>Quick Links</h4><ul><li>Lorem ipsum dolor</li><li>Amet consectetuer</li><li>Mauris vel tortor vitae</li><li>Nibh condimentum</li></ul></div>
  <div class="footer-col" style="left:562px"><h4>Support</h4><ul><li>Nibh condimentum</li><li>Integer ac lacus</li><li>Sociis natoque</li><li>Enatibus et magnis</li></ul></div>
  <div class="footer-col" style="left:732px"><h4>Newsletter:</h4></div>
</footer>
<div class="newsletter-input">Enter your email here</div>
<div class="subscribe">SUBSCRIBE</div>

</body>
</html>
```